Adept Corvana Recruitment company

We require a website for job recruitment company called "Adept Corvana"
Our company is specialising in recruitment of skilled labour from Sri Lanka into Australian market.
We would like to include a job advertising plugin where jobs can be listed and applied for .
COPYWRITING MUST BE INCLUDED !

Industry/Entity Type

Recruitment

Coding

Coded - Design and coding required

Number of Pages Required

5+ page

Colors

Designer to choose colors to be used in the design.

```html
<!DOCTYPE html>
<html lang="en">
<head>
<meta charset="utf-8">
<title>Adept Corvana – Recruitment</title>
<link href="https://fonts.googleapis.com/css2?family=Rubik:ital,wght@0,300;0,400;0,500;0,600;1,400&display=swap" rel="stylesheet">
<style>
:root{
  --blue:#0d4a9c;
  --blue-dark:#093a7e;
  --blue-light:#2e6bbf;
  --ink:#333a44;
  --muted:#6b717a;
  --grey-btn:#54575c;
  --band:#f3f4f6;
  --white:#ffffff;
  --line:#e1e3e7;
}
*{margin:0;padding:0;box-sizing:border-box}
html,body{width:1200px;height:4823px;overflow:hidden}
body{font-family:'Rubik',sans-serif;color:var(--ink);background:var(--white);position:relative}
.abs{position:absolute}
.btn{position:absolute;display:flex;align-items:center;justify-content:center;border-radius:20px;font-size:11px;font-weight:500;color:var(--white);background:var(--blue);box-shadow:0 3px 6px rgba(0,0,0,.15)}
.btn.grey{background:var(--grey-btn)}
.btn.white{background:var(--white);color:var(--blue)}
.title{position:absolute;left:0;width:1200px;text-align:center;font-size:27px;font-weight:400;color:var(--ink)}
.title b,.accent{color:var(--blue);font-weight:500}
p{font-size:11.5px;line-height:21px;color:var(--muted)}

/* header */
.brand{left:148px;top:26px;font-size:38px;font-weight:600;color:var(--ink);letter-spacing:-.5px}
.call{left:745px;top:27px;font-size:13px;color:var(--blue)}
.call span{color:var(--ink)}
.nav a{position:absolute;top:70px;font-size:11.5px;color:var(--ink);text-decoration:none}
.nav a.active{color:var(--blue)}

/* hero */
.hero-text{top:193px;left:0;width:1200px;text-align:center;font-size:34px;font-weight:300;color:var(--white);line-height:44px}
.hero-text b{font-weight:500}

/* looking */
.look h3{position:absolute;font-size:26px;font-weight:300;width:500px;text-align:center}
.look p{position:absolute;text-align:center;width:400px}

/* jobs */
.card{position:absolute;top:1835px;width:280px;height:400px;background:var(--white);box-shadow:0 3px 14px rgba(0,0,0,.08)}
.card .ph{height:174px;position:relative}
.card .lab{position:absolute;left:0;bottom:0;width:200px;height:37px;background:rgba(40,40,40,.78);color:var(--white);font-size:14px;font-weight:500;padding:10px 18px}
.card h4{margin:18px 20px 8px;font-size:13px;font-weight:500;color:var(--ink)}
.card p{margin:0 20px;font-size:10.5px;line-height:15px}
.card .link{display:block;margin:14px 20px 0;font-size:10.5px;color:var(--muted);text-decoration:underline}

/* steps */
.step{position:absolute;top:2505px;width:200px;text-align:center}
.step .ring{width:100px;height:100px;margin:0 auto;border-radius:50%;border:2px solid var(--blue);position:relative;background:var(--white)}
.step .num{position:absolute;left:40px;bottom:-10px;width:20px;height:20px;border-radius:50%;background:var(--blue);color:var(--white);font-size:10px;display:flex;align-items:center;justify-content:center}
.step h5{margin-top:24px;font-size:13px;font-weight:500}
.step p{font-size:10.5px;line-height:16px;margin:6px 12px 0}

/* blogs */
.post{position:absolute;top:3885px;width:212px;height:305px;background:var(--white);box-shadow:0 3px 14px rgba(0,0,0,.08)}
.post .ph{height:105px}
.post .by{margin:20px 20px 0;font-size:10.5px;color:var(--blue);font-weight:500}
.post h4{margin:8px 20px 0;font-size:13px;font-weight:500;line-height:18px}
.post p{margin:14px 20px 0;font-size:10.5px;line-height:16px}
.post .go{position:absolute;left:20px;bottom:-12px;width:28px;height:28px;border-radius:50%;background:var(--grey-btn);display:flex;align-items:center;justify-content:center}
.post .go.on{background:var(--blue)}

/* footer */
.flinks a{display:block;font-size:11px;color:var(--ink);text-decoration:none;margin-bottom:12px}
.social{position:absolute;top:4595px;width:30px;height:30px;border-radius:50%;background:#b9bcc2}
.social.on{background:var(--blue)}
</style>
</head>
<body>

<!-- Header -->
<div class="abs brand">Adept Corvana</div>
<div class="abs call">Call Us: <span>&#9742; 123-456-7890</span></div>
<div class="btn" style="left:930px;top:19px;width:120px;height:33px">Consult Now</div>
<nav class="nav">
  <a class="active" style="left:433px">-- Home --</a>
  <a style="left:519px">About Us</a>
  <a style="left:601px">For Employees</a>
  <a style="left:715px">For Employers</a>
  <a style="left:826px">Testimonials</a>
  <a style="left:927px">Blogs</a>
  <a style="left:991px">Contact Us</a>
</nav>

<!-- Hero -->
<svg class="abs" style="left:0;top:107px" width="1200" height="370" role="img" aria-label="Office desk with laptop, blue toned photo">
  <defs><linearGradient id="hg" x1="0" y1="0" x2="1" y2="1"><stop offset="0" stop-color="#2d68b5"/><stop offset="1" stop-color="#0b3f87"/></linearGradient></defs>
  <path d="M0 0H1200V300C1080 250 960 300 820 330C650 365 500 290 340 300C200 308 90 350 0 360Z" fill="url(#hg)"/>
  <path d="M0 360C120 320 230 300 360 305C520 312 640 370 820 340C960 316 1090 270 1200 300V320C1090 290 960 340 820 360C640 390 500 330 360 325C230 320 120 345 0 370Z" fill="#6f9bd4" opacity=".45"/>
</svg>
<div class="abs hero-text">Recruitment company with the <b>focus on</b><br><b>Sri Lanka/ Australia Market.</b></div>
<div class="btn white" style="left:540px;top:296px;width:120px;height:34px">Consult Now</div>
<svg class="abs" style="left:594px;top:416px" width="12" height="14"><path d="M6 1V12M2 8L6 12L10 8" stroke="var(--blue)" stroke-width="1.3" fill="none"/></svg>

<!-- Looking for -->
<section class="look">
  <svg class="abs" style="left:320px;top:565px" width="90" height="92" fill="none" stroke="var(--blue)" stroke-width="2.5">
    <circle cx="36" cy="18" r="12"/><path d="M10 90V55C10 44 20 38 36 38C52 38 62 44 62 55"/><path d="M30 40L36 60L42 40"/>
    <rect x="46" y="56" width="40" height="32" rx="3"/><path d="M58 56V50H74V56M46 70H86"/>
  </svg>
  <svg class="abs" style="left:778px;top:565px" width="92" height="92" fill="none" stroke="var(--blue)" stroke-width="2.5">
    <circle cx="46" cy="16" r="11"/><circle cx="20" cy="24" r="10"/><circle cx="72" cy="24" r="10"/>
    <path d="M26 90V50C26 40 34 34 46 34C58 34 66 40 66 50V90M2 90V58C2 48 8 42 18 42M90 90V58C90 48 84 42 74 42M40 36L46 52L52 36"/>
  </svg>
  <h3 style="left:115px;top:673px">Looking for a <span class="accent">Job?</span></h3>
  <h3 style="left:574px;top:673px">Looking for <span class="accent">Employees?</span></h3>
  <p style="left:165px;top:726px">Our ability to match the right employee with the right employer<br>has helped many candidates in making life changing move to Australia<br>and to become PERMANENT RESIDENT of Australia.</p>
  <p style="left:624px;top:726px">We know, how difficult it is to get the skilled labour force to help with<br>business growth and expansion . That is why Adept Corvana team is here<br>to help you . We search, screen and select only the best suitable<br>candidates with all documents ready to apply for visa which will<br>dramatically save your time and money.<br><u style="color:var(--blue);font-weight:500">Call us today</u> and let us help you expand your business.</p>
  <div class="abs" style="left:600px;top:570px;width:1px;height:350px;background:var(--line)"></div>
  <div class="btn" style="left:290px;top:878px;width:154px;height:34px">Get Your Future</div>
  <div class="btn grey" style="left:747px;top:878px;width:154px;height:34px">Find the Best Talent</div>
</section>

<!-- About band -->
<svg class="abs" style="left:0;top:990px" width="1200" height="120"><path d="M0 50C200 0 400 60 600 50C800 40 1000 10 1200 60V120H0Z" fill="var(--band)"/></svg>
<div class="abs" style="left:0;top:1100px;width:1200px;height:520px;background:var(--band)"></div>
<div class="abs" style="left:247px;top:1176px;font-size:25px">Adept <span class="accent">Corvana</span></div>
<p class="abs" style="left:247px;top:1228px;width:330px">Lorem Ipsum is simply dummy text of the printing and typesetting industry. Lorem Ipsum has been the industry's standard dummy text ever since the 1500s, when an unknown printer took a galley of type and scrambled it to make a type specimen book. It has survived not only five centuries, but also the leap into electronic typesetting, remaining.<br><br>It was popularised in the 1960s with the release of Letraset sheets containing Lorem Ipsum passages, and more recently with desktop publishing ...</p>
<div class="btn grey" style="left:247px;top:1485px;width:105px;height:33px">About Us</div>
<div class="abs" role="img" aria-label="Business people signing documents at a meeting table" style="left:599px;top:1123px;width:354px;height:452px;background:linear-gradient(135deg,#c9c4bd,#8a8580 55%,#e9e7e4)"></div>

<!-- Jobs -->
<svg class="abs" style="left:0;top:1590px" width="1200" height="80"><path d="M0 40C250 0 450 70 700 50C900 35 1050 10 1200 30V0H0Z" fill="var(--band)"/></svg>
<div class="abs" style="left:0;top:1620px;width:1200px;height:760px;background:var(--band);z-index:-1"></div>
<div class="title" style="top:1768px">Job <b>opportunities</b></div>
<div class="card" style="left:150px">
  <div class="ph" role="img" aria-label="Site supervisors in hard hats reviewing plans" style="background:linear-gradient(135deg,#8ea3b3,#c8a868)"><div class="lab">Production Supervisor</div></div>
  <h4>Job Description:</h4><p>It is a long established fact that a reader will be distracted by the readable content of a page when looking at its layout. The point of using Lorem Ipsum ...</p>
  <span class="link">www.corvanaroles.com</span>
</div>
<div class="card" style="left:462px">
  <div class="ph" role="img" aria-label="Salesperson in a busy retail store" style="background:linear-gradient(135deg,#b87c5a,#6a4d6e)"><div class="lab">Salesman</div></div>
  <h4>Job Description:</h4><p>It is a long established fact that a reader will be distracted by the readable content of a page when looking at its layout. The point of using Lorem Ipsum ...</p>
  <span class="link">www.corvanaroles.com</span>
</div>
<div class="card" style="left:770px">
  <div class="ph" role="img" aria-label="Engineer in hard hat beside industrial robot" style="background:linear-gradient(135deg,#4a4f58,#c78a2e)"><div class="lab">Industrial Engineer</div></div>
  <h4>Job Description:</h4><p>It is a long established fact that a reader will be distracted by the readable content of a page when looking at its layout. The point of using Lorem Ipsum ...</p>
  <span class="link">www.corvanaroles.com</span>
</div>
<div class="btn grey" style="left:170px;top:2175px;width:100px;height:32px">Read More</div>
<div class="btn" style="left:482px;top:2175px;width:100px;height:32px">Read More</div>
<div class="btn grey" style="left:790px;top:2175px;width:100px;height:32px">Read More</div>
<div class="btn" style="left:547px;top:2275px;width:105px;height:34px">View All</div>

<!-- Steps -->
<div class="title" style="top:2444px">One stop for your industrial <b>skilled people</b></div>
<div class="step" style="left:82px"><div class="ring">
  <svg class="abs" style="left:33px;top:33px" width="34" height="34" fill="none" stroke="var(--ink)" stroke-width="1.6"><rect x="3" y="5" width="26" height="24"/><path d="M7 11H17M7 15H17M7 19H17M7 23H25M20 10H26V20H20Z"/></svg>
  <div class="num">1</div></div><h5>Advertise job posts</h5><p>It is a long established fact that a reader will.</p></div>
<div class="step" style="left:291px"><div class="ring">
  <svg class="abs" style="left:33px;top:32px" width="34" height="36" fill="none" stroke="var(--ink)" stroke-width="1.6"><path d="M7 3H21L28 10V33H7Z M21 3V10H28M12 16H23M12 21H23M12 26H23"/></svg>
  <div class="num">2</div></div><h5>Collect applications</h5><p>It is a long established fact that a reader will.</p></div>
<div class="step" style="left:499px"><div class="ring">
  <svg class="abs" style="left:33px;top:32px" width="34" height="36" fill="none" stroke="var(--ink)" stroke-width="1.6"><rect x="6" y="5" width="23" height="28"/><path d="M13 3H22V8H13ZM10 14H12M15 14H25M10 20H12M15 20H25M10 26H12M15 26H25"/></svg>
  <div class="num">3</div></div><h5>Shortlist candidates</h5><p>It is a long established fact that a reader will.</p></div>
<div class="step" style="left:709px"><div class="ring">
  <svg class="abs" style="left:30px;top:34px" width="40" height="32" fill="none" stroke="var(--ink)" stroke-width="1.6"><path d="M3 12L12 4L20 8L28 4L37 12L22 27C20 29 18 29 16 27Z M14 12L20 8M12 18L18 24"/></svg>
  <div class="num">4</div></div><h5>Organize interviews</h5><p>It is a long established fact that a reader will.</p></div>
<div class="step" style="left:920px"><div class="ring">
  <svg class="abs" style="left:30px;top:36px" width="40" height="28" fill="none" stroke="var(--ink)" stroke-width="1.8"><path d="M2 16L9 23L24 6M14 20L17 23L32 6M30 20L38 12"/></svg>
  <div class="num">5</div></div><h5>Get permits &amp; immigration</h5><p>It is a long established fact that a reader will.</p></div>
<div class="btn" style="left:539px;top:2719px;width:122px;height:34px">Consult Now</div>

<!-- Blue band + testimonials -->
<svg class="abs" style="left:0;top:2810px" width="1200" height="800" role="img" aria-label="Crowd of commuters walking, blue toned photo">
  <defs><linearGradient id="bg2" x1="0" y1="0" x2="1" y2="1"><stop offset="0" stop-color="#0b3f87"/><stop offset=".6" stop-color="#124f9f"/><stop offset="1" stop-color="#0a3a7c"/></linearGradient></defs>
  <path d="M0 110C150 70 250 0 420 15C560 28 620 90 800 90C980 90 1080 40 1200 30V480C1000 470 800 480 600 500C400 520 200 620 0 780Z" fill="url(#bg2)"/>
</svg>
<div class="abs" style="left:247px;top:2984px;font-size:34px;font-weight:300;color:var(--white);line-height:41px">Are you Skilled with Industrial<br>work and <b style="font-weight:500">Dream to Fly all the way</b><br><b style="font-weight:500">to Australia?</b></div>
<div class="btn white" style="left:247px;top:3137px;width:120px;height:33px">Submit Details</div>
<div class="abs" role="img" aria-label="White silhouette figure in a suit" style="left:852px;top:3108px;width:78px;height:178px;background:rgba(255,255,255,.92);border-radius:39px 39px 4px 4px"></div>

<div class="title" style="top:3336px">Happy <b>clients say</b></div>
<div class="abs" style="left:560px;top:3396px;width:80px;height:80px;border-radius:50%;border:2px solid var(--blue);display:flex;align-items:center;justify-content:center;background:var(--white)">
  <div style="width:56px;height:56px;border-radius:50%;background:var(--blue);color:var(--white);font-size:34px;font-weight:600;text-align:center;line-height:64px">&ldquo;</div>
</div>
<p class="abs" style="left:270px;top:3486px;width:660px;text-align:center;font-style:italic;font-size:12.5px;line-height:21px">" It is a long established fact that a reader will be distracted by the readable content<br>of a page when looking at its layout. The point of using Lorem Ipsum is that it has a more-or-less normal<br>distribution of letters, as opposed to using 'Content here, content here', making it look like<br>readable English Many desktop. "</p>
<div class="abs" style="left:0;top:3590px;width:1200px;text-align:center;font-size:12.5px;color:var(--blue);font-weight:500">Dana Merrow</div>
<div class="abs" style="left:0;top:3609px;width:1200px;text-align:center;font-size:10px;color:var(--muted)">Salesman</div>
<svg class="abs" style="left:146px;top:3518px" width="16" height="26"><path d="M13 2L3 13L13 24" stroke="var(--blue)" stroke-width="1.6" fill="none"/></svg>
<svg class="abs" style="left:1038px;top:3518px" width="16" height="26"><path d="M3 2L13 13L3 24" stroke="var(--blue)" stroke-width="1.6" fill="none"/></svg>
<div class="btn grey" style="left:550px;top:3660px;width:100px;height:34px">View All</div>

<!-- Blogs -->
<div class="abs" style="left:0;top:3764px;width:1200px;height:640px;background:var(--band)"></div>
<div class="title" style="top:3825px">Latest <b>blogs</b></div>
<div class="post" style="left:247px"><div class="ph" role="img" aria-label="Construction workers on scaffolding at sunset" style="background:linear-gradient(135deg,#5d6e7c,#d49a4a)"></div>
  <div class="by">By Dolor Sit Amet</div><h4>Lorem ipsum has been the standard</h4><p>Sed ut perspiciatis unde omnis iste natus error sit voluptatem accusantium doloremque laudantium, totam ...</p><div class="go"><svg width="12" height="10"><path d="M1 5H10M6 1L10 5L6 9" stroke="#fff" stroke-width="1.4" fill="none"/></svg></div></div>
<div class="post" style="left:494px"><div class="ph" role="img" aria-label="Worker welding with sparks" style="background:linear-gradient(135deg,#3b4a5a,#e0822f)"></div>
  <div class="by">By Dolor Sit Amet</div><h4>Lorem ipsum has been the standard</h4><p>Sed ut perspiciatis unde omnis iste natus error sit voluptatem accusantium doloremque laudantium, totam ...</p><div class="go on"><svg width="12" height="10"><path d="M1 5H10M6 1L10 5L6 9" stroke="#fff" stroke-width="1.4" fill="none"/></svg></div></div>
<div class="post" style="left:741px"><div class="ph" role="img" aria-label="Mechanic working on a car engine" style="background:linear-gradient(135deg,#2c3138,#8b97a5)"></div>
  <div class="by">By Dolor Sit Amet</div><h4>Lorem ipsum has been the standard</h4><p>Sed ut perspiciatis unde omnis iste natus error sit voluptatem accusantium doloremque laudantium, totam ...</p><div class="go"><svg width="12" height="10"><path d="M1 5H10M6 1L10 5L6 9" stroke="#fff" stroke-width="1.4" fill="none"/></svg></div></div>
<div class="btn grey" style="left:539px;top:4236px;width:120px;height:34px">View All Blog</div>

<!-- Footer -->
<svg class="abs" style="left:0;top:4330px" width="1200" height="120"><path d="M0 60C200 20 420 90 640 70C850 50 1020 20 1200 50V120H0Z" fill="#e6e8ec"/></svg>
<div class="abs" style="left:0;top:4440px;width:1200px;height:383px;background:#e6e8ec"></div>
<div class="abs" style="left:148px;top:4505px;font-size:34px;font-weight:600;color:var(--ink);letter-spacing:-.5px">Adept Corvana</div>
<div class="social" style="left:193px"></div>
<div class="social on" style="left:234px"></div>
<div class="social" style="left:277px"></div>
<div class="abs" style="left:474px;top:4494px;font-size:12.5px;font-weight:500">Quick Links</div>
<div class="abs flinks" style="left:474px;top:4530px">
  <a>Home</a><a>About Us</a><a>For Employees</a><a>For Employers</a><a>Testimonials</a><a>Blogs</a><a>Contact Us</a>
</div>
<div class="abs" style="left:685px;top:4494px;font-size:12.5px;font-weight:500">Sign Up Newsletter</div>
<div class="abs" style="left:670px;top:4533px;width:380px;height:34px;border:1px solid #b9bcc2;border-radius:20px;font-size:10.5px;color:var(--muted);padding:10px 20px">Enter your Email ...</div>
<div class="btn" style="left:670px;top:4585px;width:105px;height:33px">Submit</div>
<div class="abs" style="left:148px;top:4748px;width:902px;height:1px;background:#c9ccd2"></div>
<div class="abs" style="left:148px;top:4780px;font-size:10.5px;color:var(--ink)">© 2022 <span class="accent">Adept Corvana</span> &nbsp;|&nbsp; All Right Reserved</div>
<svg class="abs" style="left:1114px;top:4772px" width="22" height="26"><path d="M11 1L21 25L11 19L1 25Z" fill="var(--blue)"/></svg>

</body>
</html>
```